Lumvex Crating Business Card

Project Overview
We are seeking a modern, minimalist business card that effectively represents our company while making a bold and lasting impression. The design should reflect trust, professionalism, and innovation, reinforcing our expertise in custom plastic manufacturing for warehouse and distribution centers.

Provided Assets & Specifications
Logo: We will provide our official logo for integration into the design.
Design Files: Photoshop (PSD) files for our printing specifications will be supplied.

Card Size & Material:
Dimensions: 3.5" x 2"
Material: 1/8" Radius Plastic Business Cards with 1/8" Rounded Corners
Clear plastic background—the design should strategically incorporate transparency.
Orientation: The card should be designed in landscape format for a sleek and professional presentation.

Design Requirements:
Logo Prominence
The logo must be the focal point of the card.
Space should be used effectively to draw attention to the logo while maintaining a minimalist layout.

Clear Plastic Integration
The transparent background should create the illusion of blank space, enhancing the modern and high-quality feel.
Avoid any frosted effects—we do not want white areas to appear semi-transparent.

Minimalist & Impactful
Clean, structured, and easy to read at a glance.
Focus on sharp contrast to ensure legibility and visibility.
The design should instill confidence and reflect our role as a leading plastics manufacturer.

Color Palette & Contrast
Primary Colors: Blue, Black, White, and Grey
Use bold black or blue for text and key elements to ensure they stand out against the clear plastic.
Avoid light, pastel, or neon colors that may fade into the plastic background.
No frosted or semi-transparent white—we do not want a cloudy effect.

Typography & Information Hierarchy
Bold, modern typography—clear, professional, and highly legible.
The business card should highlight:
Company Logo (Primary Focus)
Full Name & Title
Phone Number
Email
Website

Brand Representation
The card should reflect our expertise in manufacturing high-quality custom plastics for large-scale packaging and distribution businesses.
Our clients rely on us to enhance their brand presence through custom plastic solutions, and our business cards should reinforce that sense of precision and trust.

Final Considerations
Utilize the clear plastic effectively to differentiate our brand from standard business cards.
Maintain a sleek, professional aesthetic while ensuring all text and elements remain legible.
The design should align with our industry, conveying reliability and innovation.
We look forward to seeing a design that captures our brand identity, maximizes the clear plastic medium, and makes a strong, professional impact on our clients.

```html
<!DOCTYPE html>
<html lang="en">
<head>
<meta charset="utf-8">
<title>Lumvex Crating Business Card</title>
<link href="https://fonts.googleapis.com/css2?family=Montserrat:wght@500;700&display=swap" rel="stylesheet">
<style>
  :root {
    --page-bg: #e9edf1;
    --card-clear: #f4f6f8;
    --card-edge: #c9d1d8;
    --brand-blue: #3a7ab0;
    --ink-dark: #2b2b2d;
    --ink-grey: #46484c;
  }
  * { margin: 0; padding: 0; box-sizing: border-box; }
  html, body {
    width: 1200px;
    height: 900px;
    overflow: hidden;
    background: var(--page-bg);
    font-family: "Montserrat", sans-serif;
  }
  .card {
    position: absolute;
    left: 280px;
    top: 203px;
    width: 748px;
    height: 427px;
    border-radius: 14px;
    background: var(--card-clear);
    border: 1px solid var(--card-edge);
    color: var(--ink-grey);
  }
  .brand {
    position: absolute;
    left: 37px;
    top: 76px;
    height: 80px;
    display: flex;
    align-items: center;
    gap: 18px;
  }
  .brand-square {
    width: 80px;
    height: 80px;
    background: var(--brand-blue);
  }
  .brand-name {
    font-weight: 700;
    font-size: 36px;
    letter-spacing: 0.5px;
    color: var(--ink-dark);
    white-space: nowrap;
  }
  .person {
    position: absolute;
    left: 37px;
    top: 232px;
  }
  .person-name {
    font-weight: 700;
    font-size: 28px;
    line-height: 34px;
    color: var(--brand-blue);
  }
  .person-title {
    font-weight: 500;
    font-size: 19px;
    line-height: 23px;
    margin-top: 4px;
  }
  .contact {
    position: absolute;
    left: 37px;
    top: 317px;
    list-style: none;
    font-weight: 500;
    font-size: 19px;
  }
  .contact li {
    display: flex;
    align-items: center;
    gap: 12px;
    height: 29px;
    white-space: nowrap;
  }
  .contact svg { width: 20px; height: 20px; fill: var(--ink-grey); flex: none; }
  .address {
    position: absolute;
    right: 36px;
    top: 333px;
    text-align: right;
    font-weight: 500;
    font-size: 18px;
    line-height: 33px;
    color: var(--ink-dark);
    font-style: normal;
    white-space: nowrap;
  }
</style>
</head>
<body>
  <section class="card">
    <div class="brand">
      <span class="brand-square"></span>
      <span class="brand-name">Lumvex Crating</span>
    </div>

    <div class="person">
      <h1 class="person-name">Dana Whitlow</h1>
      <p class="person-title">Owner</p>
    </div>

    <ul class="contact">
      <li>
        <svg viewBox="0 0 24 24" aria-hidden="true"><path d="M6.6 10.8a15.1 15.1 0 0 0 6.6 6.6l2.2-2.2a1 1 0 0 1 1-.25 11.4 11.4 0 0 0 3.6.57 1 1 0 0 1 1 1V20a1 1 0 0 1-1 1A17 17 0 0 1 3 4a1 1 0 0 1 1-1h3.5a1 1 0 0 1 1 1c0 1.25.2 2.45.57 3.57a1 1 0 0 1-.25 1z"/></svg>
        <span>555-014-2368</span>
      </li>
      <li>
        <svg viewBox="0 0 24 24" aria-hidden="true"><path d="M2 5h20v14H2zm2 2v.5l8 5 8-5V7l-8 5z"/></svg>
        <span>info@lumvex.com</span>
      </li>
      <li>
        <svg viewBox="0 0 24 24" aria-hidden="true"><path d="M12 2a10 10 0 1 0 0 20 10 10 0 0 0 0-20zm6.9 6h-2.9a15.6 15.6 0 0 0-1.4-3.6A8 8 0 0 1 18.9 8zM12 4c.8 1.2 1.5 2.5 1.9 4h-3.8c.4-1.5 1.1-2.8 1.900-4zM4.3 14a8 8 0 0 1 0-4h3.4a16 16 0 0 0 0 4zm.8 2h2.9c.3 1.3.8 2.5 1.4 3.6A8 8 0 0 1 5.1 16zM8 8H5.1a8 8 0 0 1 4.3-3.6C8.8 5.5 8.3 6.7 8 8zm4 12c-.8-1.2-1.5-2.5-1.9-4h3.8c-.4 1.5-1.1 2.8-1.9 4zm2.3-6H9.7a14.5 14.5 0 0 1 0-4h4.6a14.5 14.5 0 0 1 0 4zm.3 5.6c.6-1.1 1.1-2.3 1.4-3.6h2.9a8 8 0 0 1-4.3 3.6zM16.3 14a16 16 0 0 0 0-4h3.4a8 8 0 0 1 0 4z"/></svg>
        <span>lumvexcrating.com</span>
      </li>
    </ul>

    <address class="address">
      88 Dockside Freight Way<br>
      Northbridge, USA
    </address>
  </section>
</body>
</html>
```